Update Business Card Design

I'm looking to update my business cards. Attached is a photo of the current design. I like the black side so that does not have to be update. The white side needs to be updated. I want the design to be modern and minimalistic.
I am a lawyer and my firm's website is www.brennoxlegalco.com (for reference).
My firm's logo has a horizontal version (which is on the black side of the card) and a vertical version (on the white side). I would prefer to keep the vertical version on the white side and horizontal version on the black side (the logo files are attached).

I am open to redesigning the black side also. I would like one side to have the horizontal logo and the other to have the vertical logo.

```html
<!DOCTYPE html>
<html lang="en">
<head>
<meta charset="utf-8">
<title>Brennox Legal Co. – Business Card</title>
<link rel="stylesheet" href="https://fonts.googleapis.com/css2?family=Arimo:wght@400;700&family=Montserrat:wght@700&family=Cinzel:wght@400&display=swap">
<style>
  :root {
    --backdrop: #4a4a4a;
    --card-white: #ffffff;
    --card-black: #1d1d1c;
    --brand-blue: #00b4e0;
    --band-dark: #04a3cc;
    --band-light: #16d4ff;
    --text-gray: #555555;
    --text-dark: #1a1a1a;
    --rule-gray: #666666;
    --site-light: #e4e4e4;
  }
  * { margin: 0; padding: 0; box-sizing: border-box; }
  html, body { width: 1200px; height: 1059px; overflow: hidden; }
  body { background: var(--backdrop); position: relative; font-family: "Arimo", Arial, sans-serif; }

  .card { position: absolute; width: 737px; height: 421px; overflow: hidden; }
  .card--front { left: 232px; top: 91px; background: var(--card-white); }
  .card--back { left: 231px; top: 546px; background: var(--card-black); }

  .firm-mark { position: absolute; left: 30px; top: 24px; width: 56px; height: 56px; background: var(--brand-blue); }
  .firm-rule { position: absolute; left: 21px; top: 183px; width: 176px; height: 3px; background: var(--rule-gray); border-radius: 2px; }
  .firm-name { position: absolute; left: 28px; top: 200px; color: var(--brand-blue); font-weight: 700; font-size: 34px; line-height: 40px; letter-spacing: 0.5px; }

  .address { position: absolute; left: 28px; top: 302px; color: var(--text-gray); font-size: 19px; line-height: 27px; }
  .office-lines { position: absolute; left: 28px; top: 369px; font-size: 19px; color: var(--text-dark); }
  .office-lines .label { color: var(--brand-blue); font-weight: 700; }
  .office-lines .divider { color: var(--brand-blue); margin: 0 12px; }

  .person { position: absolute; left: 388px; top: 18px; }
  .person-name { font-family: "Montserrat", Arial, sans-serif; font-weight: 700; font-size: 33px; color: var(--brand-blue); line-height: 36px; }
  .person-title { font-size: 19px; color: var(--text-gray); margin-top: 4px; }
  .contact { list-style: none; margin-top: 18px; }
  .contact li { display: flex; align-items: center; font-size: 19px; color: var(--text-dark); height: 29px; }
  .contact svg { width: 18px; height: 18px; margin-right: 9px; flex: none; }

  .accent-band { position: absolute; left: 0; bottom: 0; width: 100%; height: 15px;
    background: linear-gradient(90deg, var(--band-dark) 0%, var(--band-light) 55%, var(--band-dark) 100%); }

  .back-lockup { position: absolute; left: 0; top: 130px; width: 100%; display: flex; justify-content: center; align-items: center; gap: 22px; }
  .back-mark { width: 70px; height: 70px; background: var(--brand-blue); }
  .back-name { color: var(--brand-blue); font-weight: 700; font-size: 38px; line-height: 44px; letter-spacing: 1px; }
  .back-site { position: absolute; left: 0; top: 256px; width: 100%; text-align: center; font-family: "Cinzel", Georgia, serif; font-size: 21px; color: var(--site-light); letter-spacing: 0.5px; }
</style>
</head>
<body>
  <section class="card card--front">
    <div class="firm-mark"></div>
    <div class="firm-rule"></div>
    <div class="firm-name">BRENNOX<br>LEGAL CO.</div>

    <p class="address">518 N. Alder Court, Suite 304<br>Westbrook, CA 90412</p>
    <p class="office-lines"><span class="label">T.</span> 310.555.0179<span class="divider">|</span><span class="label">F.</span> 310.555.0163</p>

    <div class="person">
      <h1 class="person-name">DARIEN HOLLOWAY</h1>
      <p class="person-title">Attorney at Law</p>
      <ul class="contact">
        <li>
          <svg viewBox="0 0 24 24" aria-hidden="true"><path fill="#00b4e0" d="M6.6 10.8a15.1 15.1 0 0 0 6.6 6.6l2.2-2.2c.3-.3.7-.4 1-.2 1.1.4 2.3.6 3.6.6.6 0 1 .4 1 1V20c0 .6-.4 1-1 1C10.6 21 3 13.4 3 4c0-.6.4-1 1-1h3.5c.6 0 1 .4 1 1 0 1.3.2 2.5.6 3.6.1.3 0 .7-.2 1z"/></svg>
          310.555.0142
        </li>
        <li>
          <svg viewBox="0 0 24 24" aria-hidden="true"><path fill="#00b4e0" d="M22 2 2 11l7 3 3 8z"/></svg>
          darien@BrennoxLegalCo.com
        </li>
      </ul>
    </div>

    <div class="accent-band"></div>
  </section>

  <section class="card card--back">
    <div class="back-lockup">
      <div class="back-mark"></div>
      <div class="back-name">BRENNOX<br>LEGAL CO.</div>
    </div>
    <p class="back-site">WWW.BRENNOXLEGALCO.COM</p>
  </section>
</body>
</html>
```